Banner ad set for hotel in Portland, Oregon

We need a set of 3 banner ads for our Portland hotel advertising $20 off per night.

Ad Sizes:

300x250
728x90
160x600

Content:

Logo - Hotel Marlow
Logo - Birchfield Hospitality
Leading Copy - $20 Off per Night!
Sub Copy - 24 hour cancellations
Sub Copy - No up-front charges
Button - Check Availability
Photo - Lobby

Website (for reference):

www.hotelmarlowstay.example

```html
<!DOCTYPE html>
<html lang="en">
<head>
<meta charset="utf-8">
<title>Hotel Marlow – $20 Off Per Night Banner Set</title>
<link href="https://fonts.googleapis.com/css2?family=Arimo:wght@400;700&display=swap" rel="stylesheet">
<style>
  :root {
    --stage: #6b5d52;
    --panel: #3b3a3a;
    --panel-glass: rgba(40, 40, 42, 0.82);
    --promo-yellow: #f4ee2c;
    --ink: #1c1c1c;
    --ink-soft: #4a4f57;
    --white: #ffffff;
    --gold: #c9b23a;
    --photo-night: #1f3347;
    --photo-city: #5d7f9a;
    --photo-amber: #d9a531;
    --photo-magenta: #b4247e;
    --photo-wood: #8a5a2b;
  }
  * { box-sizing: border-box; margin: 0; padding: 0; }
  html, body { width: 1200px; height: 1000px; overflow: hidden; }
  body {
    position: relative;
    background: var(--stage);
    font-family: "Arimo", Arial, sans-serif;
  }
  .banner {
    position: absolute;
    overflow: hidden;
    box-shadow: 0 6px 14px rgba(0,0,0,0.45);
    background: var(--panel);
  }
  .lobby-photo {
    position: absolute;
    background:
      radial-gradient(ellipse at 72% 70%, rgba(217,165,49,0.85) 0%, rgba(217,165,49,0) 45%),
      radial-gradient(ellipse at 22% 72%, rgba(180,36,126,0.75) 0%, rgba(180,36,126,0) 35%),
      linear-gradient(180deg, var(--photo-wood) 0%, var(--photo-night) 28%, var(--photo-city) 48%, var(--photo-night) 62%, var(--photo-wood) 100%);
  }
  .promo-box {
    position: absolute;
    background: var(--promo-yellow);
    color: var(--ink);
    font-weight: 700;
    text-transform: uppercase;
    letter-spacing: -0.5px;
  }
  .promo-box .amount { display: block; color: var(--ink); }
  .promo-box .per-night { display: block; color: var(--ink-soft); }
  .terms {
    color: var(--white);
    font-weight: 700;
    text-align: center;
    line-height: 1.3;
  }
  .cta {
    display: block;
    background: var(--promo-yellow);
    color: var(--ink);
    font-weight: 700;
    text-align: center;
    text-transform: uppercase;
    border-radius: 8px;
  }
  .site-url {
    color: var(--promo-yellow);
    font-weight: 700;
    text-align: center;
    text-transform: uppercase;
  }
  .brand-hotel {
    color: var(--gold);
    font-weight: 400;
    text-align: center;
    letter-spacing: 2px;
    text-transform: uppercase;
  }
  .brand-group {
    display: flex;
    flex-direction: column;
    align-items: center;
    color: var(--white);
    font-weight: 400;
    text-align: center;
    text-transform: uppercase;
    letter-spacing: 2px;
  }
  .brand-group .mark-circle {
    border: 2px solid var(--white);
    border-radius: 50%;
  }

  /* 300x250 — shown large */
  .banner--rectangle { left: 33px; top: 57px; width: 905px; height: 755px; }
  .banner--rectangle .lobby-photo { inset: 0; }
  .banner--rectangle .promo-box {
    left: 0; top: 73px; width: 439px; height: 228px;
    padding: 42px 0 0 28px; font-size: 70px; line-height: 0.98;
  }
  .banner--rectangle .brand-strip {
    position: absolute; left: 0; top: 539px; width: 379px; height: 216px;
    background: var(--panel);
  }
  .banner--rectangle .offer-strip {
    position: absolute; left: 379px; top: 539px; width: 526px; height: 216px;
    background: var(--panel-glass);
  }
  .banner--rectangle .brand-hotel {
    position: absolute; left: 30px; top: 88px; width: 150px; font-size: 24px; line-height: 1.2;
  }
  .banner--rectangle .brand-group {
    position: absolute; left: 200px; top: 52px; width: 160px; font-size: 14px; gap: 10px;
  }
  .banner--rectangle .brand-group .mark-circle { width: 54px; height: 54px; }
  .banner--rectangle .terms { position: absolute; left: 0; top: 20px; width: 100%; font-size: 25px; }
  .banner--rectangle .cta {
    position: absolute; left: 105px; top: 100px; width: 334px; height: 57px;
    line-height: 57px; font-size: 25px;
  }
  .banner--rectangle .site-url { position: absolute; left: 0; top: 176px; width: 100%; font-size: 17px; }

  /* 160x600 */
  .banner--skyscraper { left: 964px; top: 103px; width: 201px; height: 754px; }
  .banner--skyscraper .brand-strip {
    position: absolute; left: 0; top: 0; width: 100%; height: 130px;
    display: flex; align-items: center; justify-content: space-around; padding: 0 8px;
  }
  .banner--skyscraper .brand-hotel { width: 80px; font-size: 13px; line-height: 1.2; letter-spacing: 1px; }
  .banner--skyscraper .brand-group { width: 90px; font-size: 8px; gap: 5px; letter-spacing: 1px; }
  .banner--skyscraper .brand-group .mark-circle { width: 26px; height: 26px; }
  .banner--skyscraper .promo-box {
    left: 0; top: 130px; width: 100%; height: 107px;
    padding: 22px 0 0 12px; font-size: 35px; line-height: 0.98;
  }
  .banner--skyscraper .promo-box .per-night { font-size: 28px; color: var(--ink); }
  .banner--skyscraper .lobby-photo { left: 0; top: 237px; width: 100%; height: 405px; }
  .banner--skyscraper .offer-strip {
    position: absolute; left: 0; top: 642px; width: 100%; height: 112px; background: var(--panel);
  }
  .banner--skyscraper .terms { position: absolute; left: 0; top: 14px; width: 100%; font-size: 13px; }
  .banner--skyscraper .cta {
    position: absolute; left: 21px; top: 50px; width: 157px; height: 28px;
    line-height: 28px; font-size: 13px; border-radius: 5px;
  }
  .banner--skyscraper .site-url { position: absolute; left: 0; top: 88px; width: 100%; font-size: 8px; }

  /* 728x90 */
  .banner--leaderboard { left: 33px; top: 831px; width: 905px; height: 111px; }
  .banner--leaderboard .offer-strip {
    position: absolute; left: 0; top: 0; width: 207px; height: 100%; background: var(--panel);
  }
  .banner--leaderboard .terms { position: absolute; left: 0; top: 16px; width: 100%; font-size: 13px; line-height: 1.3; }
  .banner--leaderboard .cta {
    position: absolute; left: 34px; top: 54px; width: 155px; height: 27px;
    line-height: 27px; font-size: 13px; border-radius: 5px;
  }
  .banner--leaderboard .site-url { position: absolute; left: 0; top: 89px; width: 100%; font-size: 8px; }
  .banner--leaderboard .lobby-photo { left: 207px; top: 0; width: 308px; height: 100%; }
  .banner--leaderboard .promo-box {
    left: 515px; top: 0; width: 215px; height: 100%;
    padding: 22px 0 0 14px; font-size: 37px; line-height: 0.98;
  }
  .banner--leaderboard .promo-box .amount { color: var(--photo-wood); }
  .banner--leaderboard .promo-box .per-night { font-size: 30px; color: var(--photo-wood); }
  .banner--leaderboard .brand-strip {
    position: absolute; left: 730px; top: 0; width: 175px; height: 100%;
    display: flex; align-items: center; justify-content: space-around; padding: 0 6px;
  }
  .banner--leaderboard .brand-hotel { width: 72px; font-size: 12px; line-height: 1.2; letter-spacing: 1px; }
  .banner--leaderboard .brand-group { width: 82px; font-size: 7px; gap: 5px; letter-spacing: 1px; }
  .banner--leaderboard .brand-group .mark-circle { width: 24px; height: 24px; }
</style>
</head>
<body>

  <section class="banner banner--rectangle" aria-label="300 by 250 banner">
    <div class="lobby-photo" role="img" aria-label="Hotel lobby with tufted gold banquette, flowers and night city skyline mural"></div>
    <div class="promo-box">
      <span class="amount">$20 Off</span>
      <span class="per-night">Per Night!</span>
    </div>
    <div class="brand-strip">
      <div class="brand-hotel">Hotel Marlow</div>
      <div class="brand-group"><span class="mark-circle"></span><span>Birchfield Hospitality</span></div>
    </div>
    <div class="offer-strip">
      <p class="terms">24 HOUR CANCELLATIONS<br>No UP-FRONT CHARGES</p>
      <a class="cta">Check Availability</a>
      <p class="site-url">www.hotelmarlowstay.example</p>
    </div>
  </section>

  <section class="banner banner--skyscraper" aria-label="160 by 600 banner">
    <div class="brand-strip">
      <div class="brand-hotel">Hotel Marlow</div>
      <div class="brand-group"><span class="mark-circle"></span><span>Birchfield Hospitality</span></div>
    </div>
    <div class="promo-box">
      <span class="amount">$20 Off</span>
      <span class="per-night">Per Night!</span>
    </div>
    <div class="lobby-photo" role="img" aria-label="Hotel lobby with tufted gold banquette, flowers and night city skyline mural"></div>
    <div class="offer-strip">
      <p class="terms">24 HOUR CANCELLATIONS<br>No UP-FRONT CHARGES</p>
      <a class="cta">Check Availability</a>
      <p class="site-url">www.hotelmarlowstay.example</p>
    </div>
  </section>

  <section class="banner banner--leaderboard" aria-label="728 by 90 banner">
    <div class="offer-strip">
      <p class="terms">24 HOUR CANCELLATIONS<br>No UP-FRONT CHARGES</p>
      <a class="cta">Check Availability</a>
      <p class="site-url">www.hotelmarlowstay.example</p>
    </div>
    <div class="lobby-photo" role="img" aria-label="Hotel lobby with flowers and night city skyline mural"></div>
    <div class="promo-box">
      <span class="amount">$20 Off</span>
      <span class="per-night">Per Night!</span>
    </div>
    <div class="brand-strip">
      <div class="brand-hotel">Hotel Marlow</div>
      <div class="brand-group"><span class="mark-circle"></span><span>Birchfield Hospitality</span></div>
    </div>
  </section>

</body>
</html>
```